Pathwell | An Alcolohism Recovery Blogging Site

Pathwell.com.au is a blog based on alcoholism. Primarily, alcholics who are in sobreity, or recovery. The blog posts are centred around this and are written by other alcholics who share their thoughts, strenght, experience, thoeries on how to get sober, and stay sober, but primarily, live a better life in active sobriety. The site provides information related to CR and other services/groups that assist in alcolohism. We write E-Books and sell these also. Pathwell strives to be a blog that alcoholics want to read, and get strength and hope from reading it, and the posts from other users. We want to be easy to use, simple to navigate and sharply designed. We want the site to be cutting edge and appealing. We want to engage the audience from the first moment they hit the page, no matter where they land. I like this website as a model for a wordpress site making good use of simplicity = thriftlane.com.au

Target Market(s)

People who might think they have a problem with Alcohol, people who are alcholics looking at entering rehab or recovery, people that are alcoholics in recovery already

Requirements
Must have
• simplicity, large fonts for headings, space for advertising through ad words and other forms, nice large navigation across the top, a sharp, html 5 feel, i want to be using great fonts and nice/sheek.
Nice to have
• logo will be used in print as well as online. It would be VERY GOOD to have someone design a ecover for my ebook i will be selling on this website. the book is titled "THE CLEAR MORNING PROMISE - The Gentle Path to finding calm and keeping it for good!"
Should not have
• do not include illustrations of alcohol.

```html
<!DOCTYPE html>
<html lang="en">
<head>
<meta charset="utf-8">
<title>Pathwell | Recovery Blog</title>
<link rel="stylesheet" href="https://fonts.googleapis.com/css2?family=Arimo:ital,wght@0,400;0,700;1,700&family=Oswald:wght@400;500&display=swap">
<style>
:root{
  --navy:#0d3758;
  --navy-deep:#0a2c47;
  --orange:#e07a1c;
  --gold:#efb04a;
  --cream:#fcd985;
  --cream-soft:#fde7a8;
  --ink:#111;
  --title:#0d3b55;
  --link:#1a3fa8;
  --ad-green:#2a8a2a;
  --white:#fff;
}
*{box-sizing:border-box;margin:0;padding:0}
html,body{width:790px;height:1200px;overflow:hidden;background:var(--white)}
body{font-family:"Arimo",Arial,sans-serif;color:var(--ink)}
.page{position:relative;width:790px;height:1200px;overflow:hidden}

/* header */
.site-header{position:absolute;left:0;top:0;width:790px;height:140px;background:var(--navy)}
.brand{position:absolute;left:20px;top:26px;display:flex;align-items:center;gap:8px;color:var(--orange);font-weight:700;font-size:36px;letter-spacing:1px}
.brand-mark{width:14px;height:14px;background:var(--orange)}
.ad-banner{position:absolute;display:flex;background:linear-gradient(90deg,#3d3d3d,#8a8a8a 35%,#2a2a2a 60%,#1e1e1e);overflow:hidden}
.ad-banner .ad-photo{width:48%;height:100%;background:linear-gradient(90deg,#2e2e2e,#9a9a9a 55%,#5c5c5c)}
.ad-banner .ad-copy{flex:1;position:relative;color:var(--white)}
.ad-banner .ad-head{position:absolute;left:8px;top:4px;font-weight:700;font-size:30px;color:#9ad0ff}
.ad-banner .ad-tag{position:absolute;left:10px;top:40px;font-weight:700;font-size:14px}
.ad-banner .ad-site{position:absolute;right:8px;top:5px;font-size:10px}
.ad-banner .ad-foot{position:absolute;left:0;right:0;bottom:0;height:12px;background:#0b2340;font-size:8px;display:flex;justify-content:space-between;padding:1px 4px}
.ad-banner.top{left:206px;top:16px;width:564px;height:66px}
.ad-banner.bottom{left:110px;top:1073px;width:565px;height:70px}

.main-nav{position:absolute;left:24px;top:108px;width:750px;display:flex;justify-content:space-between;font-size:20px;color:var(--white)}
.main-nav .current{color:var(--orange);font-weight:700}

/* hero */
.hero{position:absolute;left:21px;top:146px;width:543px;height:250px;border:2px solid var(--gold);background:linear-gradient(180deg,#8fb6dd,#d3e2ef 60%,#b7cde0)}
.hero-photo{position:absolute;left:0;top:0;width:230px;height:246px;background:linear-gradient(180deg,#a9c4de,#8fbf4a 45%,#5a7aa0)}
.hero-title{position:absolute;left:226px;top:60px;font-style:italic;font-weight:700;font-size:27px;color:var(--white)}
.hero-text{position:absolute;left:226px;top:102px;width:296px;padding:6px 10px;background:rgba(150,160,170,.75);font-size:10.5px;line-height:1.4;color:#111}
.social{position:absolute;left:236px;top:212px;display:flex;gap:20px;font-weight:700;font-size:18px}
.social span{display:flex;align-items:center;gap:8px}
.social i{display:block;width:22px;height:22px;background:var(--navy)}

/* posts */
.post{position:absolute;left:23px;width:540px}
.post h2{font-size:27px;font-weight:700;color:var(--title);margin-bottom:18px}
.post-meta{display:flex;justify-content:space-between;font-size:12.5px;margin-bottom:14px}
.post-meta .date{color:var(--orange);font-weight:700;font-size:14px}
.post-meta a{color:var(--orange);text-decoration:none}
.post p{font-size:9.6px;line-height:1.42;margin-bottom:9px}
.read-more{color:var(--orange);font-size:11.5px}
.divider{position:absolute;left:47px;width:496px;height:1px;background:#f3d9a5}

/* sidebar */
.sidebar{position:absolute;left:574px;top:0;width:194px}
.search{position:absolute;left:2px;top:172px;display:flex;gap:6px}
.search .field{width:128px;height:20px;border:1px solid #ccc;font-size:13px;font-style:italic;padding:1px 4px}
.search .go{width:54px;height:18px;border:1px solid #888;background:#eee;font-size:13px;text-align:center;margin-top:2px}
.newsletter{position:absolute;left:0;top:216px;width:194px;height:173px;background:var(--cream);border-radius:12px;text-align:center}
.newsletter h3{font-family:"Oswald",Arial,sans-serif;font-weight:400;color:var(--orange);font-size:20px;line-height:1.2;margin-top:22px}
.newsletter .sub{font-family:"Oswald",Arial,sans-serif;color:var(--title);font-size:15px;margin-top:14px}
.newsletter .row{display:flex;gap:6px;justify-content:center;margin-top:14px}
.newsletter .row .field{width:104px;height:20px;background:var(--white);border:1px solid #bbb}
.newsletter .row .btn{width:70px;height:20px;background:#eee;border:1px solid #888;font-size:12px;line-height:18px}
.box{position:absolute;left:0;width:194px;border:2px solid var(--gold);background:var(--cream)}
.box h3{background:var(--gold);color:var(--white);font-weight:700;font-size:20px;text-align:center;height:36px;line-height:36px}
.box ul{list-style:none;padding:8px 8px 0 6px}
.recent li{position:relative;padding-left:16px;margin-bottom:8px;font-size:11px;line-height:1.3}
.recent li a{color:var(--link);text-decoration:underline}
.box li::before{content:"";position:absolute;left:2px;top:3px;border-left:8px solid var(--white);border-top:6px solid transparent;border-bottom:6px solid transparent}
.archives li{position:relative;padding-left:16px;font-size:13px;font-weight:700;color:var(--title);line-height:18.5px}
.archives li::before{top:3px}
.ad-unit{position:absolute;left:0;top:614px;width:194px;height:203px;border:1px solid #f0cf86;padding:12px 4px 0}
.ad-unit .ad{margin-bottom:16px;font-size:8.3px;line-height:1.3}
.ad-unit .ad b{display:block;color:var(--link);text-decoration:underline;font-size:9.3px}
.ad-unit .ad em{font-style:normal;color:var(--ad-green)}
.ad-unit .badge{position:absolute;right:3px;bottom:6px;background:var(--link);color:var(--white);font-size:8px;padding:2px 6px;border-radius:6px 0 0 6px}

/* footer */
.site-footer{position:absolute;left:0;top:1145px;width:790px;height:55px;background:var(--navy-deep);color:var(--white);font-size:10.5px}
.footer-nav{position:absolute;left:24px;top:18px;display:flex;gap:8px}
.footer-nav .current{color:var(--orange)}
.copyright{position:absolute;right:22px;top:10px;text-align:right;line-height:1.5}
</style>
</head>
<body>
<div class="page">
  <header class="site-header">
    <div class="brand"><span class="brand-mark"></span>Pathwell</div>
    <div class="ad-banner top">
      <div class="ad-photo" role="img" aria-label="Advertising photo of an athlete stretching"></div>
      <div class="ad-copy">
        <span class="ad-head">Be Fit.</span>
        <span class="ad-tag">Natural Health for Better Living.</span>
        <span class="ad-site">fitmonth.com</span>
        <div class="ad-foot"><span>www.fitmonth.com</span><span>Feedback - Ads by Adnet</span></div>
      </div>
    </div>
    <nav class="main-nav">
      <span class="current">HOME</span><span>SUPPORT GROUPS</span><span>E-BOOK STORE</span><span>ABOUT US</span><span>CONTACT US</span>
    </nav>
  </header>

  <section class="hero">
    <div class="hero-photo" role="img" aria-label="Photo of a man with arms spread wide against a bright sky"></div>
    <h1 class="hero-title">Lorem Ipsum Dolor</h1>
    <p class="hero-text">Lorem ipsum dolor sit amet, consectetur adipiscing elit. Fusce non placerat tortor. Sed augue felis, adipiscing id cursus vel, fermentum vitae nulla. Nam eu neque mauris, vel tristique massa. Nullam auctor vehicula urna, sed vulputate dui aliquet quis! Vestibulum vulputate neque dui, id mollis augue.</p>
    <div class="social"><span><i></i>Become a fan</span><span><i></i>Follow us</span></div>
  </section>

  <article class="post" style="top:415px">
    <h2>Lorem ipsum dolor sit amet</h2>
    <div class="post-meta"><span class="date">April 11th, 2010</span><span>Posted In <a href="#">Recovery</a> &nbsp;| &nbsp;<a href="#">No Comments</a></span></div>
    <p>Lorem ipsum dolor sit amet, consectetur adipiscing elit. Fusce non placerat tortor. Sed augue felis, adipiscing id cursus vel, fermentum vitae nulla. Nam eu neque mauris, vel tristique massa. Nullam auctor vehicula urna, sed vulputate dui aliquet quis! Vestibulum vulputate neque dui, id mollis augue. Nulla in nisi a enim dignissim feugiat. Suspendisse potenti. Aliquam risus elit, pretium quis scelerisque in, ultricies quis massa. Aliquam convallis laoreet risus, sed sollicitudin odio vehicula non. Suspendisse accumsan faucibus justo; in dapibus erat tempus et! Morbi non imperdiet neque? Lorem ipsum dolor sit amet, consectetur adipiscing elit. Donec vel consectetur risus. Etiam lobortis tempor metus ut condimentum.</p>
    <span class="read-more">Read More &raquo;</span>
  </article>
  <div class="divider" style="top:623px"></div>

  <article class="post" style="top:642px">
    <h2>Lorem ipsum dolor sit amet</h2>
    <div class="post-meta"><span class="date">April 11th, 2010</span><span>Posted In <a href="#">Recovery</a> &nbsp;| &nbsp;<a href="#">No Comments</a></span></div>
    <p>Lorem ipsum dolor sit amet, consectetur adipiscing elit. Fusce non placerat tortor. Sed augue felis, adipiscing id cursus vel, fermentum vitae nulla. Nam eu neque mauris, vel tristique massa. Nullam auctor vehicula urna, sed vulputate dui aliquet quis! Vestibulum vulputate neque dui, id mollis augue. Nulla in nisi a enim dignissim feugiat. Suspendisse potenti. Aliquam risus elit, pretium quis scelerisque in, ultricies quis massa. Aliquam convallis laoreet risus, sed sollicitudin odio vehicula non. Suspendisse accumsan faucibus justo; in dapibus erat tempus et! Morbi non imperdiet neque? Lorem ipsum dolor sit amet, consectetur adipiscing elit. Donec vel consectetur risus. Etiam lobortis tempor metus ut condimentum.</p>
    <span class="read-more">Read More &raquo;</span>
  </article>
  <div class="divider" style="top:850px"></div>

  <article class="post" style="top:869px">
    <h2>Lorem ipsum dolor sit amet</h2>
    <div class="post-meta"><span class="date">April 11th, 2010</span><span>Posted In <a href="#">Recovery</a> &nbsp;| &nbsp;<a href="#">No Comments</a></span></div>
    <p>Lorem ipsum dolor sit amet, consectetur adipiscing elit. Fusce non placerat tortor. Sed augue felis, adipiscing id cursus vel, fermentum vitae nulla. Nam eu neque mauris, vel tristique massa. Nullam auctor vehicula urna, sed vulputate dui aliquet quis! Vestibulum vulputate neque dui, id mollis augue. Nulla in nisi a enim dignissim feugiat. Suspendisse potenti. Aliquam risus elit, pretium quis scelerisque in, ultricies quis massa. Aliquam convallis laoreet risus, sed sollicitudin odio vehicula non. Suspendisse accumsan faucibus justo; in dapibus erat tempus et! Morbi non imperdiet neque? Lorem ipsum dolor sit amet, consectetur adipiscing elit. Donec vel consectetur risus. Etiam lobortis tempor metus ut condimentum.</p>
    <span class="read-more">Read More &raquo;</span>
  </article>

  <aside class="sidebar">
    <div class="search"><span class="field">search</span><span class="go">Go</span></div>
    <div class="newsletter">
      <h3>SUBSCRIBE TO OUR<br>NEWSLETTER</h3>
      <p class="sub">Get notified of new posts</p>
      <div class="row"><span class="field"></span><span class="btn">Subscribe</span></div>
    </div>
    <div class="box recent" style="top:403px;height:202px">
      <h3>Recent Posts</h3>
      <ul>
        <li><a href="#">Vestibulum vulputate neque dui, id mollis</a></li>
        <li><a href="#">Vestibulum vulputate neque dui, id mollis</a></li>
        <li><a href="#">Vestibulum vulputate neque dui, id mollis</a></li>
        <li><a href="#">Vestibulum vulputate neque dui, id mollis</a></li>
      </ul>
    </div>
    <div class="ad-unit">
      <div class="ad"><b>Save on Las Vegas Hotels</b>Discount Las Vegas hotel rooms. Make your reservation today.<br><em>www.staytrail.com</em></div>
      <div class="ad"><b>Find Local Area Hotels</b>Find Local Hotels, Room Rates &amp; Much More with Localfind<br><em>www.localfind.com</em></div>
      <div class="ad"><b>Book Hotel Online</b>Find Great Deals on Hotel Rates For Your Travel Need. Book Online Today<br><em>www.roamdeal.com</em></div>
      <span class="badge">Ads by Adnet</span>
    </div>
    <div class="box archives" style="top:824px;height:230px">
      <h3>Archieves</h3>
      <ul>
        <li>December 2009</li><li>January 2010</li><li>February 2010</li><li>March 2010</li><li>April 2010</li><li>May 2010</li><li>June 2010</li><li>July 2010</li><li>August 2010</li><li>September 2010</li>
      </ul>
    </div>
  </aside>

  <div class="ad-banner bottom">
    <div class="ad-photo" role="img" aria-label="Advertising photo of an athlete stretching"></div>
    <div class="ad-copy">
      <span class="ad-head">Be Fit.</span>
      <span class="ad-tag">Natural Health for Better Living.</span>
      <span class="ad-site">fitmonth.com</span>
      <div class="ad-foot"><span>www.fitmonth.com</span><span>Feedback - Ads by Adnet</span></div>
    </div>
  </div>

  <footer class="site-footer">
    <nav class="footer-nav"><span class="current">HOME</span>|<span>SUPPORT GROUPS</span>|<span>E-BOOK STORE</span>|<span>ABOUT US</span>|<span>CONTACT US</span></nav>
    <div class="copyright">Copyright &copy; 2010 Pathwell.com.au<br>All Rights Reserved</div>
  </footer>
</div>
</body>
</html>
```